Business card design for modern LaneScope agency

Hello,

I need a business card design for my company Harbor9Studio.
We mainly offer Vornix LaneScope Tours (360° Photography) and it should be a business card with following details:

Name: Tobias Merland
Number: +49 160 55 82 907
Mail: tobias@harbor9studio.example
website: harbor9studio.example

Main colour that we use is the red of the logo.
It´s also important to integrate the "Vornix Gold logo" as the person on this business card is a Vornix Gold photographer.

And if possible we would also like to integrate something like send us a sms or pingwell and we call you back. As the number is german but we sell now in Vienna, Austria.

We offer a good price but very high photography quality, as we are mostly students - that´s our concept.

Maybe an idea is to integrate something 360° on the back-side of the card, for example the photo attached (just an idea) or some great design.
See flyer (attached) and harbor9studio.example for inspiration, maybe use of the photo of me (attached) in a circle or something

I´m very excited for your designs and thanks a lot in advance!! :)

Target Market(s)

Shops, hotels, shopping centers, etc. in Vienna, Austria

Industry/Entity Type

Business

Contact Information for Business Card

double-sided, use red of the logo, 360° vornix lanescope certified photographer

Font styles to use
Serif
Sans Serif

Colors
ec1f27

Requirements
Nice to have
• maybe some 360° design on back-side
• maybe include photo of me in a circle or something or sketched in red colour

```html
<!DOCTYPE html>
<html lang="en">
<head>
<meta charset="utf-8">
<title>Harbor9Studio Business Card</title>
<link href="https://fonts.googleapis.com/css2?family=Montserrat:wght@400;500;700;800&display=swap" rel="stylesheet">
<style>
  :root {
    --bg: #e9e9ea;
    --paper: #ffffff;
    --paper-grey: #f1f1f2;
    --brand-red: #d8173a;
    --brand-red-dark: #c8102e;
    --stripe-red: #e3412f;
    --stripe-blue: #4a86e0;
    --stripe-green: #36a853;
    --stripe-yellow: #f5b914;
    --ink: #3a3a3c;
    --white: #ffffff;
  }
  * { margin: 0; padding: 0; box-sizing: border-box; }
  html, body {
    width: 1200px; height: 726px; overflow: hidden;
    background: var(--bg);
    font-family: "Montserrat", Arial, sans-serif;
  }
  .canvas { position: relative; width: 1200px; height: 726px; }
  .card {
    position: absolute; top: 208px;
    width: 540px; height: 310px;
    background: var(--paper);
    overflow: hidden;
    box-shadow: 0 10px 28px rgba(0,0,0,0.12);
  }
  .card--back { left: 40px; }
  .card--front { left: 620px; background: linear-gradient(180deg, var(--white), var(--paper-grey)); }

  .stripe { position: absolute; left: 0; width: 100%; height: 10px; display: flex; }
  .stripe span { flex: 1; }
  .stripe .s-red { background: var(--stripe-red); }
  .stripe .s-blue { background: var(--stripe-blue); }
  .stripe .s-green { background: var(--stripe-green); }
  .stripe .s-yellow { background: var(--stripe-yellow); }

  .badge {
    position: absolute; right: 22px;
    display: flex; align-items: center; gap: 7px;
    font-weight: 500; font-size: 15px; color: var(--ink);
  }
  .badge__dot { width: 12px; height: 12px; border-radius: 50%; background: var(--stripe-green); }

  /* back side */
  .card--back .badge { top: 10px; }
  .panorama {
    position: absolute; left: 0; top: 38px; width: 100%; height: 176px;
    background:
      radial-gradient(ellipse at 70% 20%, rgba(255,255,255,0.55), transparent 55%),
      linear-gradient(160deg, #cfc7bb 0%, #a99a86 35%, #8a7a68 60%, #6d6158 100%);
  }
  .back-web {
    position: absolute; top: 232px; left: 0; width: 100%;
    text-align: center; font-size: 14px; font-weight: 500; color: var(--ink);
  }
  .back-web .accent { color: var(--brand-red); }
  .card--back .stripe { top: 274px; }

  /* front side */
  .card--front .stripe { top: 0; }
  .card--front .badge { top: 48px; }
  .front-panel {
    position: absolute; left: 0; top: 110px; width: 100%; height: 200px;
    background: linear-gradient(120deg, var(--brand-red) 0%, var(--brand-red-dark) 100%);
    color: var(--white);
  }
  .holder { position: absolute; left: 26px; top: 26px; }
  .holder__name { font-size: 30px; font-weight: 800; letter-spacing: 0.2px; line-height: 1.1; }
  .holder__role { font-size: 11px; font-weight: 400; margin-top: 4px; opacity: 0.95; }
  .contacts { position: absolute; left: 26px; bottom: 22px; list-style: none; }
  .contacts li { display: flex; align-items: center; gap: 10px; font-size: 13px; line-height: 20px; }
  .contacts svg { width: 13px; height: 13px; fill: var(--white); flex: none; }
  .studio-mark {
    position: absolute; right: 24px; top: 34px;
    display: flex; align-items: center; gap: 8px;
    font-size: 17px; font-weight: 800; color: var(--white);
  }
  .studio-mark__square { width: 22px; height: 22px; border: 3px solid var(--white); }
</style>
</head>
<body>
<main class="canvas">

  <section class="card card--back" aria-label="Business card back">
    <div class="badge"><span class="badge__dot"></span>Vornix Gold</div>
    <div class="panorama" role="img" aria-label="360° panorama of a shopping centre atrium with escalators and shops"></div>
    <p class="back-web">www.<span class="accent">harbor9studio</span>.example</p>
    <div class="stripe"><span class="s-red"></span><span class="s-blue"></span><span class="s-green"></span><span class="s-yellow"></span></div>
  </section>

  <section class="card card--front" aria-label="Business card front">
    <div class="stripe"><span class="s-red"></span><span class="s-blue"></span><span class="s-green"></span><span class="s-yellow"></span></div>
    <div class="badge"><span class="badge__dot"></span>Vornix Gold</div>
    <div class="front-panel">
      <div class="holder">
        <h1 class="holder__name">Tobias Merland</h1>
        <p class="holder__role">360° vornix lanescope certified photographer</p>
      </div>
      <div class="studio-mark"><span class="studio-mark__square"></span>Harbor9Studio</div>
      <ul class="contacts">
        <li>
          <svg viewBox="0 0 24 24" aria-hidden="true"><path d="M6.6 10.8a15.1 15.1 0 0 0 6.6 6.6l2.2-2.2a1 1 0 0 1 1-.25 11.4 11.4 0 0 0 3.6.57 1 1 0 0 1 1 1V20a1 1 0 0 1-1 1A17 17 0 0 1 3 4a1 1 0 0 1 1-1h3.5a1 1 0 0 1 1 1c0 1.25.2 2.45.57 3.57a1 1 0 0 1-.25 1z"/></svg>
          +49 160 55 82 907
        </li>
        <li>
          <svg viewBox="0 0 24 24" aria-hidden="true"><path d="M2 5h20v14H2z M4 7v.4l8 5 8-5V7l-8 5z" fill-rule="evenodd"/></svg>
          tobias@harbor9studio.example
        </li>
        <li>
          <svg viewBox="0 0 24 24" aria-hidden="true"><path d="M12 2a10 10 0 1 0 0 20 10 10 0 0 0 0-20zm6.9 6h-3a15 15 0 0 0-1.3-3.9A8 8 0 0 1 18.9 8zM12 4c.8 1.1 1.5 2.5 1.9 4h-3.8c.4-1.5 1.1-2.9 1.9-4zM4.3 14a8 8 0 0 1 0-4h3.4a16 16 0 0 0 0 4zm.8 2h3a15 15 0 0 0 1.3 3.9A8 8 0 0 1 5.1 16zm3-8h-3a8 8 0 0 1 4.3-3.9A15 15 0 0 0 8.1 8zM12 20c-.8-1.1-1.5-2.5-1.9-4h3.8c-.4 1.5-1.1 2.9-1.9 4zm2.3-6H9.7a14 14 0 0 1 0-4h4.6a14 14 0 0 1 0 4zm.3 5.9A15 15 0 0 0 15.9 16h3a8 8 0 0 1-4.3 3.9zM16.3 14a16 16 0 0 0 0-4h3.4a8 8 0 0 1 0 4z"/></svg>
          www.harbor9studio.example
        </li>
      </ul>
    </div>
  </section>

</main>
</body>
</html>
```